Corrow Family Farm fresh honey jar label

I need a label for jars of honey harvested at our farm. These are for gifts and personal use. We are looking to incorporate our farm brand into the label. We would like the design to take the existing brand and add some element like bees, honey, flowers, or hives to indicate the contents. We want the design to feel homemade and authentic without feeling cheap or hoaky

Requirements
Must have
• The label must be made to fit a 1" x2" rectangular label. The label must include the attached family brand. The label must include the text "Corrow Family Farms" "Pinebrook, USA" "Farm Fresh Honey". The label will be printed on off-white paper
Nice to have
• It would be nice to have illustrations of bees or flowers around the logo or hives or honeycombs. The label should have a vintage feel
Should not have
• The label should not feel overly cartoonish or hoaky

```html
<!DOCTYPE html>
<html lang="en">
<head>
<meta charset="utf-8">
<title>Corrow Family Farms – Farm Fresh Honey Label</title>
<link rel="stylesheet" href="https://fonts.googleapis.com/css2?family=Oswald:wght@500&family=Montserrat:wght@700;800&display=swap">
<style>
  :root {
    --cream-bg: #f8f4ea;
    --grey-bg: #eeeeee;
    --label-paper: #f8f4ea;
    --gold: #c9963f;
    --gold-light: #dcb46a;
    --ink: #231f1c;
  }
  * { margin: 0; padding: 0; box-sizing: border-box; }
  html, body { width: 1200px; height: 2339px; overflow: hidden; }
  body { position: relative; background: var(--cream-bg); }

  .panel { position: absolute; left: 0; width: 1200px; }
  .panel--top { top: 0; height: 1132px; background: var(--cream-bg); }
  .panel--bottom { top: 1132px; height: 1207px; background: var(--grey-bg); }

  .label {
    position: absolute;
    width: 280px;
    height: 596px;
    background: var(--label-paper);
    border: 3px solid var(--gold);
    border-radius: 18px;
    transform-origin: top left;
  }
  .label--hero { left: 460px; top: 270px; }
  .label--jar { left: 498px; top: 460px; transform: scale(0.73); }

  .label__inner-frame {
    position: absolute;
    inset: 5px;
    border: 1.5px solid var(--gold);
    border-radius: 12px;
  }

  .label__bee {
    position: absolute;
    top: 58px;
    width: 54px;
    height: 50px;
    border-radius: 50%;
    background: radial-gradient(circle, var(--gold) 0%, var(--gold-light) 60%, rgba(220,180,106,0) 72%);
  }
  .label__bee--left { left: 30px; }
  .label__bee--right { right: 30px; }

  .label__brand-mark {
    position: absolute;
    top: 62px;
    left: 0;
    right: 0;
    text-align: center;
    font-family: "Oswald", sans-serif;
    font-weight: 500;
    font-size: 26px;
    letter-spacing: 2px;
    color: var(--ink);
  }

  .label__divider {
    position: absolute;
    left: 50%;
    width: 96px;
    margin-left: -48px;
    height: 6px;
  }
  .label__divider::before {
    content: "";
    position: absolute;
    left: 0; right: 0; top: 2.5px;
    height: 1px;
    background: var(--gold);
  }
  .label__divider::after {
    content: "";
    position: absolute;
    left: 50%; top: 0;
    width: 6px; height: 6px;
    margin-left: -3px;
    border-radius: 50%;
    background: var(--gold);
    box-shadow: 0 0 0 3px var(--label-paper);
  }
  .label__divider--top { top: 124px; }
  .label__divider--mid { top: 341px; }
  .label__divider--low { top: 539px; width: 80px; margin-left: -40px; }

  .label__farm-name {
    position: absolute;
    top: 136px;
    left: 0; right: 0;
    text-align: center;
    font-family: "Oswald", sans-serif;
    font-weight: 500;
    font-size: 58px;
    line-height: 65px;
    letter-spacing: 3px;
    color: var(--ink);
    text-transform: uppercase;
  }

  .label__illustration {
    position: absolute;
    top: 354px;
    left: 36px;
    width 206px;
    width: 206px;
    height: 106px;
    border-radius: 40px;
    background: radial-gradient(ellipse at center, var(--gold) 0%, var(--gold-light) 55%, rgba(220,180,106,0.15) 100%);
  }

  .label__tagline {
    position: absolute;
    top: 472px;
    left: 0; right: 0;
    text-align: center;
    font-family: "Montserrat", sans-serif;
    font-weight: 700;
    font-size: 18px;
    letter-spacing: 1.5px;
    color: var(--ink);
  }
  .label__product {
    position: absolute;
    top: 490px;
    left: 0; right: 0;
    text-align: center;
    font-family: "Montserrat", sans-serif;
    font-weight: 800;
    font-size: 42px;
    letter-spacing: 2px;
    color: var(--ink);
  }
  .label__origin {
    position: absolute;
    top: 559px;
    left: 0; right: 0;
    text-align: center;
    font-family: "Montserrat", sans-serif;
    font-weight: 800;
    font-size: 11px;
    letter-spacing: 2px;
    color: var(--ink);
  }
</style>
</head>
<body>

<section class="panel panel--top">
  <div class="label label--hero">
    <div class="label__inner-frame"></div>
    <div class="label__bee label__bee--left" role="img" aria-label="Engraved gold honeybee illustration"></div>
    <div class="label__brand-mark">Corrow</div>
    <div class="label__bee label__bee--right" role="img" aria-label="Engraved gold honeybee illustration"></div>
    <div class="label__divider label__divider--top"></div>
    <h1 class="label__farm-name">Corrow<br>Family<br>Farms</h1>
    <div class="label__divider label__divider--mid"></div>
    <div class="label__illustration" role="img" aria-label="Gold engraved illustration of a dripping honeycomb with blossoms and lavender sprigs"></div>
    <p class="label__tagline">FARM FRESH</p>
    <p class="label__product">HONEY</p>
    <div class="label__divider label__divider--low"></div>
    <p class="label__origin">PINEBROOK, USA</p>
  </div>
</section>

<section class="panel panel--bottom">
  <div class="label label--jar">
    <div class="label__inner-frame"></div>
    <div class="label__bee label__bee--left" role="img" aria-label="Engraved gold honeybee illustration"></div>
    <div class="label__brand-mark">Corrow</div>
    <div class="label__bee label__bee--right" role="img" aria-label="Engraved gold honeybee illustration"></div>
    <div class="label__divider label__divider--top"></div>
    <p class="label__farm-name">Corrow<br>Family<br>Farms</p>
    <div class="label__divider label__divider--mid"></div>
    <div class="label__illustration" role="img" aria-label="Gold engraved illustration of a dripping honeycomb with blossoms and lavender sprigs"></div>
    <p class="label__tagline">FARM FRESH</p>
    <p class="label__product">HONEY</p>
    <div class="label__divider label__divider--low"></div>
    <p class="label__origin">PINEBROOK, USA</p>
  </div>
</section>

</body>
</html>
```